Lose Up To 1 LB Of Fat Per Day

We need a double sided street sign for our weight loss clinic. We need the doctors picture to the right side of the sign and we need a challenge “Lose Up To 1 Pound Of Fat Per Day” included in the signage.
Our color scheme for the clinic are black, white, teal and silver.
The phone number should be at the bottom of the sign
555-206–3948

Target Market(s)

Weight Loss

Font styles to use
Sans Serif

```html
<!DOCTYPE html>
<html lang="en">
<head>
<meta charset="utf-8">
<title>Weight Loss Clinic Street Sign</title>
<link rel="stylesheet" href="https://fonts.googleapis.com/css2?family=Khand:wght@400;600&display=swap">
<style>
  :root {
    --teal: #128680;
    --teal-light: #bfe0dd;
    --white: #ffffff;
    --ink: #111111;
    --backdrop: #d9d9d9;
    --photo-top: #c9d6e4;
    --photo-bottom: #8fa6bd;
  }
  html, body {
    margin: 0;
    width: 1200px;
    height: 1200px;
    overflow: hidden;
    background: var(--backdrop);
  }
  .canvas {
    position: relative;
    width: 1200px;
    height: 1200px;
  }
  .sign {
    position: absolute;
    left: 80px;
    top: 340px;
    width: 1040px;
    height: 520px;
    overflow: hidden;
    background: var(--white);
  }
  .sign-shapes {
    position: absolute;
    inset: 0;
    width: 100%;
    height: 100%;
  }
  .headline {
    position: absolute;
    left: 78px;
    top: 108px;
    margin: 0;
    font-family: "Khand", sans-serif;
    font-weight: 400;
    color: var(--ink);
    line-height: 1;
  }
  .headline span { display: block; }
  .headline-lead { font-size: 48px; }
  .headline-main { font-size: 62px; margin-top: 6px; }
  .headline-main strong { font-weight: 600; color: var(--teal); }
  .headline-tail { font-size: 62px; margin-top: 4px; }
  .phone {
    position: absolute;
    left: 76px;
    top: 330px;
    display: flex;
    align-items: center;
    gap: 14px;
    font-family: "Khand", sans-serif;
    font-size: 46px;
    font-weight: 400;
    color: var(--ink);
    line-height: 1;
  }
  .phone-icon { width: 36px; height: 36px; }
</style>
</head>
<body>
<div class="canvas">
  <div class="sign">
    <svg class="sign-shapes" viewBox="0 0 827 414" preserveAspectRatio="none">
      <defs>
        <linearGradient id="doctorPhotoTone" x1="0" y1="0" x2="0" y2="1">
          <stop offset="0" stop-color="var(--photo-top)"/>
          <stop offset="1" stop-color="var(--photo-bottom)"/>
        </linearGradient>
      </defs>
      <rect class="teal-field" width="827" height="414" fill="var(--teal)"/>
      <path class="white-field" fill="var(--white)"
        d="M0,0 H190 C330,48 480,74 630,77 V337 C480,340 330,366 190,414 H0 Z"/>
      <g class="dot-grid" fill="var(--teal)">
        <circle cx="14" cy="11" r="1.6"/><circle cx="29" cy="11" r="1.6"/><circle cx="44" cy="11" r="1.6"/><circle cx="59" cy="11" r="1.6"/>
        <circle cx="14" cy="33" r="1.6"/><circle cx="29" cy="33" r="1.6"/><circle cx="44" cy="33" r="1.6"/><circle cx="59" cy="33" r="1.6"/>
        <circle cx="14" cy="54" r="1.6"/><circle cx="29" cy="54" r="1.6"/><circle cx="44" cy="54" r="1.6"/><circle cx="59" cy="54" r="1.6"/>
      </g>
      <g class="hatch-lines" stroke="var(--teal-light)" stroke-width="2.5">
        <line x1="114" y1="377" x2="124" y2="359"/><line x1="126" y1="377" x2="136" y2="359"/>
        <line x1="138" y1="377" x2="148" y2="359"/><line x1="150" y1="377" x2="160" y2="359"/>
        <line x1="162" y1="377" x2="172" y2="359"/><line x1="174" y1="377" x2="184" y2="359"/>
        <line x1="186" y1="377" x2="196" y2="359"/><line x1="198" y1="377" x2="208" y2="359"/>
      </g>
      <path class="inner-arc" fill="none" stroke="var(--teal)" stroke-width="6" stroke-linecap="round"
        d="M530,85 A156,156 0 0 0 530,329"/>
      <path class="outer-arc-top" fill="none" stroke="var(--teal)" stroke-width="3" stroke-linecap="round"
        d="M479,85 A190,190 0 0 0 446,143"/>
      <path class="outer-arc-bottom" fill="none" stroke="var(--teal)" stroke-width="3" stroke-linecap="round"
        d="M446,267 A190,190 0 0 0 479,329"/>
      <circle cx="446" cy="143" r="9" fill="var(--teal)"/>
      <circle cx="446" cy="267" r="9" fill="var(--teal)"/>
      <path class="white-arc" fill="none" stroke="var(--white)" stroke-width="3"
        d="M629,49 A158,158 0 0 1 631,364"/>
      <circle class="doctor-photo" cx="630" cy="207" r="130" fill="url(#doctorPhotoTone)"
        role="img" aria-label="Photo of the clinic doctor in a white coat holding a stethoscope"/>
    </svg>

    <h1 class="headline">
      <span class="headline-lead">Lose Up To</span>
      <span class="headline-main"><strong>1 Pound</strong> of Fat</span>
      <span class="headline-tail">Per Day</span>
    </h1>

    <div class="phone">
      <svg class="phone-icon" viewBox="0 0 36 36" aria-hidden="true">
        <circle cx="18" cy="18" r="16" fill="none" stroke="var(--teal)" stroke-width="2.5"/>
        <path fill="var(--teal)" d="M12.5,9.5 l3,0 1.5,4 -2,1.8 c1,2.4 2.8,4.2 5.2,5.2 l1.8,-2 4,1.5 0,3 c0,1.2 -1,2 -2.2,2 C16.5,25 11,19.5 10.5,11.7 c0,-1.2 0.8,-2.2 2,-2.2 z"/>
      </svg>
      <span class="phone-number">555-206–3948</span>
    </div>
  </div>
</div>
</body>
</html>
```